Email Preference Page Design

We are looking for a 2 page design for our users to edit their email preferences and submit friend referrals. You can find the fuctionality, content and text here:

https://brightcart.examplemail.net/app/linkClick/7281/5c9a1b3e8d04f2aa/20583941/7f3d9e2b1a6c4058

* the shipping and billing address might be different so you need to show the billing if the "same as shipping" box is not checked. It can auto-hide like the page above shows if that fits your design.

* when the "unsubscribe from all email lists" box is selected, all the other checkbox options will hide as in the example page. We need you to show us what the site will look like with and without that checkbox selected.

We want to match these two pages to the general feel of these website pages:

www.brightcart.com
and
free.brightcart.com

The page should be very clean and tight. Project is for design only but must be able to be implemented in html showing button and checkbox states. Technically this must be two pages for our system - one for all the user info and one for individual email referrals (see example above).

Target Market(s)

video professionals

Industry/Entity Type

Shipping

Requirements
Must have
• our logo (see numerous versions attached)
well designed header
well designed sections
clean editable text
tight layout
html friendly
easy to understand
2 pages
Nice to have
• custom checkboxes and radio buttons

```html
<!DOCTYPE html>
<html lang="en">
<head>
<meta charset="utf-8">
<title>Button States – Save My Preferences</title>
<link rel="stylesheet" href="https://fonts.googleapis.com/css2?family=Open+Sans:wght@400;600&display=swap">
<style>
  :root {
    --canvas-orange: #f99c33;
    --footer-navy: #1e2f3c;
    --label-ink: #1b1b1b;
    --button-text: #ffffff;
    --button-border: #141c22;
    --normal-top: #35495a;
    --normal-bottom: #1b2a36;
    --hover-top: #1f303d;
    --hover-bottom: #2f4a5f;
    --active-top: #8c4d0c;
    --active-bottom: #5c2f03;
    --active-border: #3a1e03;
  }
  * { box-sizing: border-box; margin: 0; padding: 0; }
  html, body {
    width: 1200px;
    height: 616px;
    overflow: hidden;
  }
  body {
    position: relative;
    background: var(--canvas-orange);
    font-family: "Open Sans", Arial, sans-serif;
  }
  .state-row {
    position: absolute;
    left: 0;
    width: 1200px;
    height: 87px;
  }
  .state-row--normal { top: 96px; }
  .state-row--hover { top: 237px; }
  .state-row--active { top: 375px; }
  .state-label {
    position: absolute;
    left: 56px;
    top: 0;
    height: 87px;
    line-height: 87px;
    font-size: 26px;
    font-weight: 400;
    color: var(--label-ink);
  }
  .save-button {
    position: absolute;
    left: 410px;
    top: 0;
    width: 529px;
    height: 87px;
    border: 1.5px solid var(--button-border);
    border-radius: 4px;
    font-family: "Open Sans", Arial, sans-serif;
    font-size: 38px;
    font-weight: 600;
    color: var(--button-text);
    letter-spacing: 0.2px;
    cursor: pointer;
    background: linear-gradient(to bottom, var(--normal-top), var(--normal-bottom));
  }
  .save-button--hover {
    background: linear-gradient(to bottom, var(--hover-top), var(--hover-bottom));
  }
  .save-button--active {
    border-color: var(--active-border);
    background: linear-gradient(to bottom, var(--active-top), var(--active-bottom));
  }
  .pointer-cursor {
    position: absolute;
    left: 674px;
    top: 308px;
    width: 26px;
    height: 34px;
  }
  .site-footer-band {
    position: absolute;
    left: 0;
    bottom: 0;
    width: 1200px;
    height: 30px;
    background: var(--footer-navy);
  }
</style>
</head>
<body>
  <main class="button-states">
    <div class="state-row state-row--normal">
      <span class="state-label">1 Normal Button</span>
      <button class="save-button" type="button">Save My Preferences</button>
    </div>
    <div class="state-row state-row--hover">
      <span class="state-label">2 Mouse-Hover Button</span>
      <button class="save-button save-button--hover" type="button">Save My Preferences</button>
    </div>
    <div class="state-row state-row--active">
      <span class="state-label">3 Mouse-Click Button</span>
      <button class="save-button save-button--active" type="button">Save My Preferences</button>
    </div>
  </main>

  <svg class="pointer-cursor" viewBox="0 0 26 34" aria-hidden="true">
    <path d="M8 2.5c1.2 0 2 .9 2 2v9.5l.3-3c.2-1 1-1.6 2-1.5 1 .1 1.7 1 1.7 2v1.5c.2-.9 1-1.5 2-1.4 1 .1 1.7 1 1.7 2v1.6c.3-.8 1-1.3 1.9-1.2 1 .1 1.8 1 1.8 2v7c0 3.5-2.6 6.5-6.6 6.5h-3.5c-2.2 0-3.6-.9-4.8-2.5L2.3 21c-.7-1-.4-2.2.5-2.8.9-.6 2-.4 2.7.4L6 20V4.5c0-1.1.8-2 2-2z"
      fill="#ffffff" stroke="#111111" stroke-width="1.4" stroke-linejoin="round"/>
    <path d="M10.5 21v5M14 21v5M17.5 21v5" stroke="#111111" stroke-width="1.2" stroke-linecap="round"/>
  </svg>

  <footer class="site-footer-band"></footer>
</body>
</html>
```